Finance web application design

We need a design for a new responsive finance web application. It should look uber professional and modern.

Inspiration and design we like:

website:
http://www.brennickhale.com/

The application presented here:
http://markets.pelvantgrid.com/en/products/tools-applications/trading-investment-tools/zarvo-trading-software.html

https://apps.quillstore.example/us/app/ferncastle-for-tablet/id582917463?mt=8

The application presented here (Slatepad version):
https://apps.quillstore.example/en/app/trevik-forex-trading/id649205318?mt=8&utm_source=trevikButton

Target Market(s)

Private Investors

Industry/Entity Type

Finance

Number of Pages Required

5+ page

Font styles to use
Other font styles liked:
• Nobile

Requirements
Must have
• Colors for "up" changes: green
• Colors for "down" changes: red
• Fonts in tables must be very easy to read -
• Deliver design for all pages attached.
Nice to have
• A dark (gray) background
• Graphs should be shaded and partly transparent - orange or blue
• White text as "normal" - orange text / blue text for headers
Should not have
• White background

```html
<!DOCTYPE html>
<html lang="en">
<head>
<meta charset="utf-8">
<title>Strategy – Tradevane</title>
<link rel="stylesheet" href="https://fonts.googleapis.com/css2?family=Open+Sans:wght@400;600;700&display=swap">
<style>
:root{
  --bg:#1e2328;
  --panel:#262c33;
  --panel-line:#353d46;
  --nav:#15191d;
  --blue:#1b79b5;
  --blue-light:#2e9be0;
  --orange:#f0962e;
  --orange-fill:rgba(240,150,46,.55);
  --text:#e9edf1;
  --muted:#8d98a3;
  --up:#3fb35a;
  --down:#d9433b;
  --compound:#5cb870;
}
*{box-sizing:border-box;margin:0;padding:0}
html,body{width:744px;height:1200px;overflow:hidden}
body{background:var(--bg);color:var(--text);font-family:"Open Sans",Arial,sans-serif;font-size:11px}
.topbar{height:40px;background:var(--nav);display:flex;align-items:center;padding:0 14px;gap:14px}
.brand{display:flex;align-items:center;gap:6px;font-size:17px;font-weight:700;color:var(--text);margin-right:6px}
.brand-dot{width:12px;height:12px;border-radius:50%;background:var(--blue-light)}
.nav{display:flex;height:40px}
.nav a{color:var(--text);text-decoration:none;font-size:10px;font-weight:600;padding:0 8px;display:flex;align-items:center}
.nav a.active{background:var(--orange);color:#fff}
.search{margin-left:auto;width:120px;height:20px;border-radius:3px;background:#2b3138;color:var(--muted);font-size:9px;padding:3px 8px}
.user{display:flex;align-items:center;gap:6px;font-size:10px}
.avatar{width:18px;height:18px;border-radius:50%;background:#59636e}
.page{padding:0 14px}
.page-title{font-size:15px;font-weight:400;margin:20px 0 24px}
.section-title{color:var(--orange);font-size:13px;font-weight:600;margin-bottom:10px}
.pnl{width:100%;border-collapse:collapse;font-size:9px;text-align:center}
.pnl th{background:var(--blue);color:#fff;font-weight:600;height:26px;border-right:1px solid #15598a}
.pnl th.compound{background:var(--compound)}
.pnl td{height:24px;border:1px solid var(--panel-line);background:var(--panel)}
.pnl td.year,.pnl th.year{background:#1a1e23;font-weight:600;width:40px}
.pnl td.up{background:var(--up)}
.pnl td.down{background:var(--down)}
.columns{display:grid;grid-template-columns:360px 342px;gap:14px;margin-top:30px}
.col{display:flex;flex-direction:column;gap:20px}
.panel{background:var(--panel)}
.panel-head{background:var(--blue);color:#fff;font-size:12px;font-weight:600;height:30px;display:flex;align-items:center;padding:0 10px}
.panel-body{padding:8px}
.chart{display:block}
.stats{list-style:none;padding:6px 10px}
.stats li{display:flex;justify-content:space-between;height:26.5px;align-items:center;border-bottom:1px solid var(--panel-line);font-size:10px}
.stats .label{flex:0 0 50%;text-align:center}
.stats .value{flex:0 0 50%;text-align:center;color:var(--orange);font-weight:600}
.positions{margin-top:24px}
.positions .panel-head{justify-content:space-between}
.btn{background:#fff;color:var(--blue);font-size:9px;font-weight:700;padding:3px 8px;border-radius:2px}
.pos-table{width:100%;border-collapse:collapse;font-size:9px}
.pos-table th{text-align:left;background:#1a1e23;color:var(--muted);font-weight:600;height:20px;padding:0 10px}
.pos-table td{height:22px;padding:0 10px;border-bottom:1px solid var(--panel-line)}
.due{text-align:right;font-size:11px;font-weight:700;margin:10px 4px}
.footer{position:absolute;left:0;right:0;top:1168px;height:32px;background:var(--nav);color:var(--muted);font-size:9px;display:flex;align-items:center;justify-content:center}
</style>
</head>
<body>
<header class="topbar">
  <div class="brand"><span class="brand-dot"></span>Tradevane</div>
  <nav class="nav">
    <a href="#">Dashboard</a><a href="#" class="active">Strategies</a><a href="#">Portfolios</a><a href="#">Market Data</a><a href="#">Cost Inst.</a><a href="#">User</a>
  </nav>
  <div class="search">Search for stocks…</div>
  <div class="user"><span class="avatar"></span>John Doe</div>
</header>

<main class="page">
  <h1 class="page-title">Strategy &lt;name&gt;</h1>
  <h2 class="section-title">Profit and Loss</h2>
  <table class="pnl">
    <thead><tr><th class="year">Year</th><th>January</th><th>February</th><th>March</th><th>April</th><th>May</th><th>June</th><th>July</th><th>August</th><th>September</th><th>October</th><th>November</th><th>December</th><th class="compound">Compound</th></tr></thead>
    <tbody>
      <tr><td class="year">2013</td><td>1,023</td><td>1,023</td><td>1,023</td><td class="down">1,023</td><td class="up">1,023</td><td>1,023</td><td>1,023</td><td>1,023</td><td>1,023</td><td>1,023</td><td>1,023</td><td>1,023</td><td>1,023</td></tr>
      <tr><td class="year">2014</td><td>1,023</td><td>1,023</td><td>1,023</td><td>1,023</td><td>1,023</td><td>1,023</td><td>1,023</td><td>1,023</td><td>1,023</td><td>1,023</td><td>1,023</td><td>1,023</td><td>1,023</td></tr>
      <tr><td class="year">2015</td><td>1,023</td><td>1,023</td><td>1,023</td><td>1,023</td><td>1,023</td><td>1,023</td><td>1,023</td><td>1,023</td><td>1,023</td><td>1,023</td><td>1,023</td><td>1,023</td><td>1,023</td></tr>
    </tbody>
  </table>

  <div class="columns">
    <div class="col">
      <section class="panel">
        <div class="panel-head">Equity Curve</div>
        <div class="panel-body">
          <svg class="chart" width="344" height="136" viewBox="0 0 344 136">
            <g stroke="#353d46" stroke-width="1"><line x1="20" y1="20" x2="340" y2="20"/><line x1="20" y1="55" x2="340" y2="55"/><line x1="20" y1="90" x2="340" y2="90"/><line x1="20" y1="122" x2="340" y2="122"/></g>
            <path d="M20 122 L20 70 L40 60 L60 66 L80 48 L100 56 L120 44 L140 52 L160 38 L180 46 L200 34 L220 42 L240 30 L260 40 L280 28 L300 36 L320 30 L340 44 L340 122 Z" fill="var(--orange-fill)"/>
            <path d="M20 70 L40 60 L60 66 L80 48 L100 56 L120 44 L140 52 L160 38 L180 46 L200 34 L220 42 L240 30 L260 40 L280 28 L300 36 L320 30 L340 44" fill="none" stroke="var(--orange)" stroke-width="1.5"/>
            <rect x="60" y="8" width="52" height="14" fill="var(--blue)"/><text x="86" y="18" fill="#fff" font-size="8" text-anchor="middle">814 Nodes</text>
            <g fill="#8d98a3" font-size="7"><text x="0" y="23">400</text><text x="0" y="58">300</text><text x="0" y="93">200</text><text x="0" y="125">100</text></g>
          </svg>
        </div>
      </section>
      <section class="panel">
        <div class="panel-head">Drawdown</div>
        <div class="panel-body">
          <svg class="chart" width="344" height="244" viewBox="0 0 344 244">
            <g stroke="#353d46"><line x1="20" y1="10" x2="340" y2="10"/><line x1="20" y1="70" x2="340" y2="70"/><line x1="20" y1="130" x2="340" y2="130"/><line x1="20" y1="190" x2="340" y2="190"/></g>
            <path d="M20 10 L40 60 L55 14 L75 150 L95 12 L115 110 L135 16 L160 70 L180 12 L205 220 L225 14 L245 95 L265 12 L285 160 L305 14 L325 80 L340 12 Z" fill="var(--orange-fill)" stroke="var(--orange)" stroke-width="1.5" stroke-linejoin="round"/>
            <rect x="180" y="198" width="52" height="14" fill="var(--blue)"/><text x="206" y="208" fill="#fff" font-size="8" text-anchor="middle">814 Nodes</text>
          </svg>
        </div>
      </section>
      <section class="panel">
        <div class="panel-head">Number Instruments Passing Filter</div>
        <div class="panel-body">
          <svg class="chart" width="344" height="128" viewBox="0 0 344 128">
            <g stroke="#353d46"><line x1="10" y1="20" x2="340" y2="20"/><line x1="10" y1="55" x2="340" y2="55"/><line x1="10" y1="90" x2="340" y2="90"/><line x1="10" y1="120" x2="340" y2="120"/></g>
            <g fill="var(--blue-light)" opacity=".85">
              <rect x="20" y="80" width="12" height="40"/><rect x="44" y="64" width="12" height="56"/><rect x="68" y="92" width="12" height="28"/><rect x="92" y="70" width="12" height="50"/><rect x="116" y="86" width="12" height="34"/><rect x="140" y="60" width="12" height="60"/><rect x="164" y="76" width="12" height="44"/><rect x="188" y="96" width="12" height="24"/><rect x="212" y="68" width="12" height="52"/><rect x="236" y="82" width="12" height="38"/><rect x="260" y="58" width="12" height="62"/><rect x="284" y="88" width="12" height="32"/><rect x="308" y="74" width="12" height="46"/>
            </g>
          </svg>
        </div>
      </section>
    </div>

    <div class="col">
      <section class="panel">
        <div class="panel-head">Statistics</div>
        <ul class="stats">
          <li><span class="label">Initial Capital</span><span class="value">1.000.000 NOK</span></li>
          <li><span class="label">Profits</span><span class="value">1.000.000 NOK</span></li>
          <li><span class="label">Comission</span><span class="value">1.000.000 NOK</span></li>
          <li><span class="label">Avg Profits / Trade</span><span class="value">1.000.000 NOK</span></li>
          <li><span class="label">Num Trade</span><span class="value">1.000.000 NOK</span></li>
          <li><span class="label">Max Drawdown Bars</span><span class="value">1.000.000 NOK</span></li>
          <li><span class="label">Max Drawdown Days</span><span class="value">1.000.000 NOK</span></li>
          <li><span class="label">Initial Capital</span><span class="value">1.000.000 NOK</span></li>
          <li><span class="label">Profits</span><span class="value">1.000.000 NOK</span></li>
          <li><span class="label">Comission</span><span class="value">1.000.000 NOK</span></li>
          <li><span class="label">Avg Profits / Trade</span><span class="value">1.000.000 NOK</span></li>
          <li><span class="label">Num Trade</span><span class="value">1.000.000 NOK</span></li>
          <li><span class="label">Max Drawdown Bars</span><span class="value">1.000.000 NOK</span></li>
          <li><span class="label">Max Drawdown Days</span><span class="value">1.000.000 NOK</span></li>
        </ul>
      </section>
      <section class="panel">
        <div class="panel-head">Market Timing</div>
        <div class="panel-body">
          <svg class="chart" width="326" height="190" viewBox="0 0 326 190">
            <g fill="var(--blue-light)" opacity=".85">
              <rect x="10" y="24" width="10" height="160"/><rect x="32" y="30" width="10" height="154"/><rect x="54" y="20" width="10" height="164"/><rect x="76" y="36" width="10" height="148"/><rect x="98" y="26" width="10" height="158"/><rect x="120" y="40" width="10" height="144"/><rect x="142" y="22" width="10" height="162"/><rect x="164" y="32" width="10" height="152"/><rect x="186" y="24" width="10" height="160"/><rect x="208" y="38" width="10" height="146"/><rect x="230" y="28" width="10" height="156"/><rect x="252" y="20" width="10" height="164"/><rect x="274" y="34" width="10" height="150"/><rect x="296" y="26" width="10" height="158"/>
            </g>
          </svg>
        </div>
      </section>
    </div>
  </div>

  <section class="panel positions">
    <div class="panel-head">Open Positions <span class="btn">View all trade ›</span></div>
    <table class="pos-table">
      <thead><tr><th>Name</th><th>ID</th><th>Quantity</th><th>Date</th></tr></thead>
      <tbody>
        <tr><td>Norvale Europe / Real Estate NR USD</td><td>NO0010345GDF</td><td>100.00</td><td>20.11.2014</td></tr>
        <tr><td>Fjellmark Tindra</td><td>NO0010345GDF</td><td>200.00</td><td>20.11.2014</td></tr>
        <tr><td>NXE Bolt Indeks</td><td>NO0010345GDF</td><td>50.00</td><td>20.11.2014</td></tr>
      </tbody>
    </table>
  </section>
  <p class="due">New Positions is due EOD 31.12.2014</p>
</main>

<footer class="footer">Copyright © 2014 Tradevane. All Rights Reserved.</footer>
</body>
</html>
```